A poster for international internet marketing exhibition event

We need a poster design for a B2B exhibition event. Main purpose of the poster is to promote the company brand and showcase our services.

Main Tag line 1: Improve Web Visibility
Main Tag line 2: Get Laser Targeted Traffic To Your Website

Through the poster, we hope to convey a fun and professional company culture.
We would like to see designs that use the colour of sky blue and white (to be in lined with our company website).

Some important information:
Services Offer: Search Engine Optimization, Search Engine Marketing, Social Media Marketing, Video Marketing, Reputation Management, Ranking Maintenance, Web Design & Development
Core Business: Search Engine Optimization

Company Name: Brookvane Pte Ltd
Website: http://www.brookvane.com.sg
Resolution: 300 dpi (minimum)
Dimension: 85cm (Width) x 200 cm (height)
Preferably in Photoshop format (.psd)

Target Market(s)

Corporate Customers. Target market will usually be business owners and marketing professionals.

Industry/Entity Type

Internet

Requirements
Must have
• The poster must show all the services that are offered. Does not require to provide description for each service.
The poster also must show company logo in prominent position.

```html
<!DOCTYPE html>
<html lang="en">
<head>
<meta charset="utf-8">
<title>Brookvane Pte Ltd – Services Poster</title>
<link rel="stylesheet" href="https://fonts.googleapis.com/css2?family=Arimo:wght@400;700&display=swap">
<style>
  :root {
    --sky-top: #5f95c9;
    --sky-mid: #9fc4e4;
    --sky-low: #cfe2f1;
    --cloud: #ffffff;
    --btn-top: #3f8fe0;
    --btn-bottom: #0b3f9a;
    --btn-edge: #8cc4f5;
    --title-yellow: #f4e82a;
    --url-red: #e8102a;
    --band-top: #2e84d6;
    --band-bottom: #0a4aa6;
    --white: #ffffff;
    --brand-ink: #1d3f7a;
  }
  * { box-sizing: border-box; margin: 0; padding: 0; }
  html, body { width: 1200px; height: 2816px; overflow: hidden; }
  body { font-family: "Arimo", Arial, sans-serif; background: var(--sky-mid); }
  .poster { position: relative; width: 1200px; height: 2816px; overflow: hidden; }

  .sky {
    position: absolute; inset: 0;
    background:
      radial-gradient(ellipse 520px 260px at 220px 380px, rgba(255,255,255,.55), transparent 70%),
      radial-gradient(ellipse 600px 300px at 950px 1300px, rgba(255,255,255,.4), transparent 70%),
      radial-gradient(ellipse 500px 260px at 200px 1700px, rgba(255,255,255,.35), transparent 70%),
      linear-gradient(180deg, var(--sky-top) 0%, var(--sky-mid) 35%, var(--sky-low) 70%, var(--sky-mid) 100%);
  }

  .floor {
    position: absolute; left: 0; top: 1880px; width: 1200px; height: 360px;
    background: linear-gradient(180deg, rgba(255,255,255,0) 0%, rgba(255,255,255,.45) 60%, rgba(255,255,255,.2) 100%);
    clip-path: polygon(22% 0, 78% 0, 100% 100%, 0 100%);
  }

  .brand {
    position: absolute; left: 40px; top: 80px; width: 420px; height: 230px;
    display: flex; align-items: center; justify-content: center;
  }
  .brand-disc {
    position: absolute; left: 0; top: 0; width: 420px; height: 230px;
    border-radius: 50%; background: var(--cloud); opacity: .9;
  }
  .brand-name {
    position: relative; font-weight: 700; font-size: 54px; letter-spacing: 1px;
    color: var(--brand-ink);
  }

  .web-bar {
    position: absolute; left: 460px; top: 258px; width: 690px; height: 80px;
    background: rgba(255,255,255,.75); border-radius: 10px;
    display: flex; align-items: center; gap: 20px; padding-left: 6px;
  }
  .search-icon {
    width: 76px; height: 70px; border-radius: 10px;
    background: linear-gradient(180deg, var(--btn-top), var(--btn-bottom));
    display: flex; align-items: center; justify-content: center;
  }
  .web-url { font-size: 44px; font-weight: 700; color: var(--url-red); letter-spacing: 1px; }

  .services-title {
    position: absolute; left: 0; width: 1200px; top: 520px; text-align: center;
    font-size: 124px; font-weight: 700; color: var(--title-yellow); letter-spacing: -2px;
    text-shadow: 0 3px 4px rgba(0,0,0,.25);
  }

  .service {
    position: absolute; width: 248px; height: 256px; border-radius: 26px;
    background: linear-gradient(180deg, var(--btn-top) 0%, #1c63c6 45%, var(--btn-bottom) 100%);
    box-shadow: inset 0 4px 0 var(--btn-edge), 0 8px 14px rgba(0,40,100,.3);
    color: var(--white); font-size: 33px; line-height: 1.2;
    padding: 38px 14px 0 24px; overflow: hidden;
  }
  .service.core { font-size: 28px; padding-left: 18px; }
  .service.large { font-size: 38px; padding-left: 18px; padding-right: 8px; }
  .col-a { left: 232px; }
  .col-b { left: 736px; }
  .row-1 { top: 792px; }
  .row-2 { top: 1132px; }
  .row-3 { top: 1484px; padding-top: 56px; }
  .row-4 { top: 1836px; padding-top: 56px; }

  .service-reflection {
    position: absolute; top: 2100px; width: 248px; height: 120px; border-radius: 0 0 26px 26px;
    background: linear-gradient(180deg, rgba(28,99,198,.35), rgba(28,99,198,0));
    color: rgba(255,255,255,.5); font-size: 38px; padding: 0 18px;
    transform: scaleY(-1); overflow: hidden;
  }

  .tagline-band {
    position: absolute; left: 0; top: 2220px; width: 1200px; height: 596px;
    background: linear-gradient(180deg, var(--band-top) 0%, var(--band-bottom) 100%);
    color: var(--white);
  }
  .tagline {
    position: absolute; font-variant: small-caps; font-weight: 700; line-height: 1;
    white-space: nowrap; font-size: 76px; letter-spacing: 1px;
  }
  .tagline.visibility { right: 40px; top: 170px; }
  .tagline.traffic { right: 40px; top: 262px; font-size: 70px; }
  .tagline.website { left: 370px; top: 366px; font-size: 70px; }
  .tagline-rule {
    position: absolute; left: 380px; top: 250px; width: 780px; height: 5px; background: var(--white);
  }
</style>
</head>
<body>
<main class="poster">
  <div class="sky" role="img" aria-label="Blue sky with soft white clouds"></div>
  <div class="floor"></div>

  <header class="brand">
    <div class="brand-disc"></div>
    <span class="brand-name">BROOKVANE</span>
  </header>

  <div class="web-bar">
    <div class="search-icon">
      <svg width="46" height="46" viewBox="0 0 46 46" aria-hidden="true">
        <circle cx="19" cy="19" r="13" fill="none" stroke="#fff" stroke-width="6"/>
        <line x1="29" y1="29" x2="42" y2="42" stroke="#fff" stroke-width="7" stroke-linecap="round"/>
      </svg>
    </div>
    <span class="web-url">www.brookvane.com.sg</span>
  </div>

  <h1 class="services-title">Services Offer</h1>

  <div class="service core col-a row-1">Search Engine Optimization (Core Business)</div>
  <div class="service col-b row-1">Search Engine Marketing</div>
  <div class="service col-a row-2">Social Media Marketing</div>
  <div class="service large col-b row-2">Video Marketing</div>
  <div class="service col-a row-3">Reputation Management</div>
  <div class="service col-b row-3">Ranking Maintenance</div>
  <div class="service large col-a row-4">Web Design</div>
  <div class="service large col-b row-4">Web Development</div>

  <div class="service-reflection col-a" aria-hidden="true">Design</div>
  <div class="service-reflection col-b" aria-hidden="true">Development</div>

  <section class="tagline-band">
    <p class="tagline visibility">Improve Web Visibility</p>
    <div class="tagline-rule"></div>
    <p class="tagline traffic">Get Laser Targeted Traffic</p>
    <p class="tagline website">To Your Website</p>
  </section>
</main>
</body>
</html>
```